Stationery Design Project - Ta fourmilière

We are a french company, Ta Fourmilière. It means Your Anthill.
We own and manage woods, we transform it industrially into very high quality (dry) logs and pellets and we commercialize them to individuals in France.
People can order the logs online or by phone and get the wood logs delivered at home.

After our great logo contest, we would like to launch a new stationery project.

Target Market(s)

inhabitants of sub-urban areas in France. (living in houses not in apartment )

Industry/Entity Type

It Company

Requirements
Must have
• content see attachment
logo

For the business card, we would like on the front side, the logo, name + contact info. We would like to use the back side for commercial purpose insisting on our distinctive value proposition.
Nice to have
• the back side of the business card can be more colorful

```html
<!DOCTYPE html>
<html lang="fr">
<head>
<meta charset="utf-8">
<title>Ta Fourmilière – Papeterie</title>
<link href="https://fonts.googleapis.com/css2?family=Poppins:wght@400;600&display=swap" rel="stylesheet">
<style>
  :root {
    --red: #c4212a;
    --ink: #3a3a3a;
    --white: #ffffff;
    --frame: #9a9a9a;
    --wood-dark: #5b4331;
    --wood-mid: #8a6446;
    --wood-light: #d9c4a6;
    --fig-main: #b0443c;
    --fig-soft: #3d5672;
  }
  * { box-sizing: border-box; margin: 0; padding: 0; }
  html, body { width: 1200px; height: 1000px; overflow: hidden; background: var(--white); }
  body { position: relative; font-family: "Poppins", sans-serif; color: var(--ink); }

  .letterhead {
    position: absolute; left: 118px; top: 82px; width: 596px; height: 843px;
    border: 1px solid var(--frame); background: var(--white); overflow: hidden;
  }
  .letterhead__band { position: absolute; left: 109px; top: 0; width: 45px; height: 100%; background: var(--red); }
  .letterhead__stripes { position: absolute; left: 154px; top: 0; width: 16px; height: 100%; display: flex; }
  .letterhead__stripes span { display: block; height: 100%; }
  .s-mid { width: 5px; background: var(--wood-mid); }
  .s-light { width: 5px; background: var(--wood-light); }
  .s-dark { width: 6px; background: var(--wood-dark); }

  .wordmark {
    position: absolute; writing-mode: vertical-rl; transform: rotate(180deg);
    font-weight: 600; color: var(--ink); line-height: 1; letter-spacing: -0.5px; white-space: nowrap;
  }
  .letterhead .wordmark { left: 18px; top: 22px; height: 148px; font-size: 19px; text-align: left; }

  .mascot {
    position: absolute; border-radius: 6px;
    background: linear-gradient(180deg, var(--fig-main) 0%, var(--fig-main) 40%, var(--fig-soft) 60%, var(--fig-soft) 100%);
    opacity: 0.85;
  }
  .letterhead .mascot { left: 44px; top: 20px; width: 82px; height: 148px; }

  .letterhead__address {
    position: absolute; left: 19px; top: 766px; width: 103px; height: 62px;
    background: var(--white); padding: 3px 4px;
    font-size: 8.4px; font-weight: 600; line-height: 1.3; color: var(--ink);
  }

  .card { position: absolute; left: 842px; width: 242px; height: 157px; overflow: hidden; }
  .card--front { top: 562px; border: 1px solid var(--frame); background: var(--white); }
  .card--front .wordmark { left: 3px; top: 3px; height: 150px; font-size: 19px; }
  .card--front .mascot { left: 26px; top: 18px; width: 72px; height: 126px; }
  .card__panel {
    position: absolute; left: 94px; top: 0; width: 147px; height: 100%;
    background: var(--red); color: var(--white); padding: 32px 0 0 25px;
  }
  .card__name { font-size: 9.5px; font-weight: 600; }
  .card__contacts { margin-top: 10px; font-size: 6.8px; line-height: 1.45; }
  .card__contacts b { font-weight: 600; }
  .card__slogan { position: absolute; left: 25px; top: 128px; font-size: 9px; font-weight: 600; }
  .card__web { position: absolute; left: 0; width: 147px; top: 142px; text-align: center; font-size: 7px; font-weight: 600; padding-left: 14px; }

  .card--back { top: 770px; background: var(--red); color: var(--white); text-align: center; }
  .card__offer { margin-top: 12px; font-size: 9.5px; font-weight: 600; line-height: 1.45; }
  .card__order { margin-top: 12px; font-size: 7.6px; font-weight: 600; line-height: 1.5; }
  .card__quality { margin-top: 10px; font-size: 7.3px; font-weight: 600; line-height: 1.5; }
  .card__stripes { position: absolute; left: 0; bottom: 0; width: 100%; }
  .card__stripes span { display: block; width: 100%; }
  .h-dark { height: 5px; background: var(--wood-dark); }
  .h-light { height: 4px; background: var(--wood-light); }
  .h-white { height: 2px; background: var(--white); }
  .h-mid { height: 4px; background: var(--wood-mid); }
  .h-red { height: 5px; background: var(--red); }
</style>
</head>
<body>

<section class="letterhead" aria-label="Papier à en-tête">
  <div class="letterhead__band"></div>
  <div class="letterhead__stripes"><span class="s-mid"></span><span class="s-light"></span><span class="s-dark"></span></div>
  <div class="wordmark">Ta Fourmilière</div>
  <div class="mascot" role="img" aria-label="Illustration de la mascotte bûcheron en chemise à carreaux portant des bûches"></div>
  <address class="letterhead__address">
    12 Chemin des Pins<br>
    69290 Craponne<br>
    Tél : 04 72 18 40 26<br>
    www.tafourmiliere.fr<br>
    info@tafourmiliere.fr
  </address>
</section>

<section class="card card--front" aria-label="Carte de visite recto">
  <div class="wordmark">Ta Fourmilière</div>
  <div class="mascot" role="img" aria-label="Illustration de la mascotte bûcheron en chemise à carreaux portant des bûches"></div>
  <div class="card__panel">
    <p class="card__name">Claire MOREAU</p>
    <p class="card__contacts">
      <b>Tél:</b> 04 72 18 40 26<br>
      <b>Mobile:</b> 04 72 18 40 26<br>
      <b>Email:</b> moreau@tafourmiliere.fr
    </p>
    <p class="card__slogan">Entre nous, ça chauffe!</p>
    <p class="card__web">www.tafourmiliere.fr</p>
  </div>
</section>

<section class="card card--back" aria-label="Carte de visite verso">
  <p class="card__offer">Livraison gratuite de bois de chauffage<br>à Lyon et sa région<br>Bûches, granulés, briquettes</p>
  <p class="card__order">Commandez sur www.tafourmiliere.fr<br>ou au 04 72 18 40 26</p>
  <p class="card__quality">Qualité supérieure, origine régionale certifiée,<br>livraison en 48h</p>
  <div class="card__stripes"><span class="h-dark"></span><span class="h-light"></span><span class="h-white"></span><span class="h-mid"></span><span class="h-red"></span></div>
</section>

</body>
</html>
```